Real Estate agent needs flyer/folder to contain bio and overview of services

I'm including files of the layout of the small folder. The folder is 6 1/2 across and 9 1/2 inches long. It will have a front & back cover and then writing on the 2 inside pages.

I am sending a few files to incorporate into the flyer, 1 new logo to use and 2 files which are coloring ideas.

Colors

Designer to choose colors to be used in the design.

```html
<!DOCTYPE html>
<html lang="en">
<head>
<meta charset="utf-8">
<title>Real Estate Folder – Inside Spread</title>
<link href="https://fonts.googleapis.com/css2?family=Nunito:wght@700;800;900&family=Quicksand:wght@400;500;600;700&display=swap" rel="stylesheet">
<style>
  :root{
    --panel-blue:#6b9bd5;
    --heading-blue:#2d52b4;
    --accent-blue:#2a57c4;
    --name-blue:#3f7fe0;
    --panel-text:#f3f6fc;
    --body-gray:#474a50;
    --heading-gray:#54575c;
    --paper:#ffffff;
  }
  *{margin:0;padding:0;box-sizing:border-box}
  html,body{width:1200px;height:821px;overflow:hidden;background:var(--paper)}
  .spread{position:relative;width:1200px;height:821px;overflow:hidden;background:var(--paper);
    font-family:"Quicksand",sans-serif;font-weight:500;font-size:11.6px;line-height:14.8px;letter-spacing:-0.1px}
  .portrait-photo{position:absolute;left:0;top:0;width:302px;height:821px;
    background:linear-gradient(180deg,#1d3a78 0%,#284d94 40%,#3762a8 70%,#2a4a88 100%)}
  .intro-panel{position:absolute;left:302px;top:0;width:301px;height:821px;background:var(--panel-blue)}

  .column{position:absolute;top:61px;display:flex;flex-direction:column}
  .column-panel{left:318px;width:262px}
  .column-sell{left:628px;width:250px}
  .column-buy{left:893px;width:248px}

  .heading{position:relative;font-family:"Nunito",sans-serif;font-weight:800;font-size:15.5px;
    line-height:20px;height:20px;margin-bottom:13px;color:var(--heading-blue);letter-spacing:.4px;white-space:nowrap}
  .heading.gray{color:var(--heading-gray)}
  .column-panel .heading::before{content:"";position:absolute;left:-10px;top:7px;width:5px;height:5px;
    border:1.3px solid var(--panel-text);border-radius:50%}

  .copy{text-align:justify}
  .copy p{margin-bottom:14.8px}
  .copy p:last-child{margin-bottom:0}
  .panel-copy{padding-left:9px;color:var(--panel-text)}
  .sell-copy{padding-left:9px;color:var(--body-gray)}
  .buy-copy{padding-left:7px;color:var(--accent-blue);font-weight:600}

  .sec-intro{min-height:345px}
  .sec-tenet{min-height:172px}
  .sec-selling{min-height:441px}
  .sec-buying{min-height:472px}
  .sec-quote-first{min-height:104px}

  .tenet-title{font-family:"Nunito",sans-serif;font-weight:900;font-size:13px;color:#fff;margin-bottom:1px;letter-spacing:0}
  .emph-blue{color:var(--heading-blue);font-weight:700}
  .panel-copy strong{font-weight:700;color:#fff}
  .testimonial{color:var(--body-gray);font-weight:500}
  .client-name{display:block;text-align:right;font-family:"Nunito",sans-serif;font-weight:800;
    color:var(--name-blue);font-size:12px;line-height:15px;letter-spacing:0}
</style>
</head>
<body>
<main class="spread">
  <div class="portrait-photo" role="img" aria-label="Portrait of the agent in front of a blue-toned palm tree streetscape"></div>
  <div class="intro-panel"></div>

  <div class="column column-panel">
    <section class="sec-intro">
      <h2 class="heading">Let me introduce myself</h2>
      <div class="copy panel-copy">
        <p>I'm originally from Chicago, but I'm a full-fledged California girl now. I've lived and worked in Orange County since 1996. I always say where we live is the next best thing to living on a tropical island. I've traveled to many and I'm always happy to come back to my Laguna Niguel home.</p>
        <p>My passion for this area is why I'm in Real Estate. I consider myself incredibly fortunate to sell homes and help people purchase homes in an area that I love with all my heart.</p>
        <p>This passion also carries over in representing my clients with the highest degree of professionalism, enthusiasm and care. My business is built on exceptional customer service and I'm grateful my clients are mostly repeat and referrals.</p>
      </div>
    </section>
    <section class="sec-tenet">
      <h2 class="heading">My Core Tenet</h2>
      <div class="copy panel-copy">
        <div class="tenet-title">It's All About YOU!</div>
        <p><span class="emph-blue">My #1 priority is understanding YOUR needs and YOUR objectives.</span> This understanding, along with working diligently on your behalf, means we accomplish your goal whether you're purchasing your 1st home or selling a home you've loved so you can move on to the next chapter of your life.</p>
      </div>
    </section>
    <section>
      <h2 class="heading">Real Estate Services &amp; Beyond...</h2>
      <div class="copy panel-copy">
        <p>Simply put, I help people who are local, relocating and investing, sell and purchase homes in Southern California. For purchases outside of California, I can refer to a network of agents across the country.</p>
        <p>I also provide a team who is dedicated to providing outstanding customer service throughout the transaction. My team includes a network of <strong>lenders</strong>, <strong>title</strong>, and <strong>escrow officers</strong>, in house <strong>CPA</strong>, <strong>stagers</strong>, <strong>photographers</strong>, <strong>contractors</strong> and more.</p>
      </div>
    </section>
  </div>

  <div class="column column-sell">
    <section class="sec-selling">
      <h2 class="heading">Selling your home</h2>
      <div class="copy sell-copy">
        <p>Selling your home is not like any other business transaction. It's also personal. My priority as your Listing Agent is to guide you through what can be a complicated and sometimes emotional process.</p>
        <p>I place great emphasis on marketing your property with professional photographs, along with harnessing the power of the Internet and the virtual world to reach as many buyers as possible. Your property will be marketed to the public as well as to other agents, thus creating maximum exposure of your home.</p>
        <p>When we first meet to discuss selling your home, it's essential for me to gain an understanding of your unique needs such as timelines, expectations and financial considerations, just to name a few. From there, I begin the process of listing and marketing your home. I lead you through negotiations and more paperwork than you ever care to do, guiding you to the successful closing of your home.</p>
      </div>
    </section>
    <section>
      <h2 class="heading">Testimonials</h2>
      <div class="copy sell-copy testimonial sec-quote-first">
        <p>Dana got us an amazing deal on our new home and sold our old home in a week. Dana is patient, hardworking, professional and most importantly HONEST. Dana is definitely one of the best in the business!</p>
        <span class="client-name">Priya &amp; Owen Hale</span>
      </div>
      <div class="copy sell-copy testimonial">
        <p>Dana is the kind of Real Estate professional everyone wants to represent them. She is knowledgeable, ethical, energetic, and follows up on every detail. Her honesty, integrity and expertise combined make her a very special and remarkable professional. We were lucky to find her!</p>
        <span class="client-name">Miles &amp; Joanna Reed</span>
      </div>
    </section>
  </div>

  <div class="column column-buy">
    <section class="sec-buying">
      <h2 class="heading gray">Buying a home</h2>
      <div class="copy buy-copy">
        <p>If you're thinking about buying a home, it's imperative you have an accomplished, real estate professional by your side to walk you through what is likely the largest purchase of your life.</p>
        <p>To get started, I like to meet with you so we have an opportunity to get to know each other as purchasing a home is a uniquely, personal endeavor. At that time, we can discuss your goals and if it's a good time for you to purchase a home.</p>
        <p>From there, the first step is to obtain a pre-approval from a lender. I'm able to recommend various lenders who can introduce and explain the various loan products available.</p>
        <p>After you've been pre-approved, that's when the fun starts! I guide you through the home buying adventure every step of the way and look forward to handing you the keys to your new home.</p>
      </div>
    </section>
    <div class="copy buy-copy testimonial">
      <p>During the home buying process, Dana becomes your trusted advisor, mentor and friend. Her knowledge of the industry, community and market are best in class. A true professional! Dana aligned her goals with my own and understood the motivation behind my purchase. Dana is unequivocally the reason why I was able to purchase my home in Laguna Niguel and provide my family with a world-class community. Without her guidance and experience, I would still be in the market attempting to navigate the ever-changing work of real estate.</p>
      <span class="client-name">Teodor Valencia</span>
    </div>
  </div>
</main>
</body>
</html>
```